amber crest health and wellness group.

need a full website design , all information provided in word document labeled website blue print

Target Market(s)

first responders, military , people in crisis

Coding

Coded - Design and coding required

Number of Pages Required

1 page

```html
<!DOCTYPE html>
<html lang="en">
<head>
<meta charset="utf-8">
<title>Amber Crest Health and Wellness Group</title>
<link rel="stylesheet" href="https://fonts.googleapis.com/css2?family=Urbanist:ital,wght@0,300;0,400;0,500;0,600;0,700;0,800;1,800&display=swap">
<style>
:root{
  --navy:#1f3f7a;
  --blue:#2c5c9a;
  --accent:#3f6fb3;
  --sky:#5ab0d8;
  --ink:#1b1b1b;
  --text:#3a3a3a;
  --muted:#5a5a5a;
  --grey:#a1a1a1;
  --black:#000;
  --white:#fff;
  --green:#35a66b;
  --badge:#dfe3e9;
}
*{margin:0;padding:0;box-sizing:border-box}
html,body{width:1200px;height:4743px;overflow:hidden}
body{font-family:"Urbanist",sans-serif;color:var(--ink);background:var(--white);position:relative}
.btn{position:absolute;display:flex;align-items:center;justify-content:center;gap:12px;border-radius:20px;font-size:13px;font-weight:600;letter-spacing:.3px;color:var(--white);background:var(--navy);text-transform:uppercase}
.btn::after{content:"";width:10px;height:10px;border-radius:50%;background:var(--white)}
.btn.small-dot::after{width:6px;height:6px}
.eyebrow{font-size:22px;font-weight:500;text-transform:uppercase;color:var(--ink)}
.photo{position:absolute;overflow:hidden}

/* nav */
.site-nav{position:absolute;left:0;top:0;width:1200px;height:74px;background:var(--black);z-index:5}
.brand{position:absolute;left:60px;top:20px;display:flex;align-items:center;gap:10px}
.brand-mark{width:34px;height:34px;border-radius:50%;background:#c9ccd2}
.brand-name{color:var(--accent);font-weight:700;font-size:17px;line-height:1;text-transform:uppercase}
.brand-name small{display:block;font-size:8px;letter-spacing:.5px;margin-top:3px}
.nav-links{position:absolute;left:258px;top:29px;display:flex;gap:21px;font-size:13px;color:#d8d8d8;text-transform:uppercase}
.nav-links .active{color:var(--accent)}
.nav-cta{left:878px;top:20px;width:219px;height:34px;background:var(--accent)}
.nav-cta::after{width:6px;height:6px}

/* hero */
.hero{position:absolute;left:0;top:74px;width:1200px;height:590px;
  clip-path:polygon(0 0,100% 0,100% 81%,50% 98.5%,0 81%);
  background:
    radial-gradient(ellipse 260px 300px at 950px 200px,rgba(226,180,150,.55),transparent 70%),
    radial-gradient(ellipse 380px 320px at 1000px 520px,#b8323a,transparent 70%),
    radial-gradient(ellipse 300px 260px at 250px 260px,#5d6670,transparent 72%),
    radial-gradient(ellipse 140px 90px at 400px 40px,#c9d34a,transparent 70%),
    linear-gradient(110deg,#8a5a2c 0%,#c48444 28%,#a7713f 50%,#8c5a3a 68%,#9d3a32 85%,#6c2a24 100%)}
.hero-shade{position:absolute;inset:0;background:rgba(0,0,0,.22)}
.hero-title{position:absolute;left:0;top:140px;width:1200px;text-align:center;color:var(--white);font-size:57px;font-weight:700;line-height:60px;text-transform:uppercase}
.hero-title em{font-weight:800;font-style:italic;display:block}
.hero-sub{position:absolute;left:0;top:304px;width:1200px;text-align:center;color:var(--white);font-size:20px;line-height:32px;font-weight:500}
.hero-cta{left:491px;top:408px;width:216px;height:35px}
.hero-edge{position:absolute;left:0;top:540px;z-index:2}
.badge{position:absolute;left:550px;top:591px;width:124px;height:124px;border-radius:50%;background:var(--black);z-index:3;display:flex;align-items:center;justify-content:center}
.badge span{width:64px;height:64px;border-radius:50%;background:#c9ccd2}

/* story */
.story-main{left:110px;top:804px;width:440px;height:490px;border-radius:10px;
  background:
    radial-gradient(ellipse 120px 220px at 60px 330px,#c8322c,transparent 75%),
    radial-gradient(ellipse 110px 200px at 380px 380px,#1f8f84,transparent 75%),
    radial-gradient(ellipse 70px 80px at 110px 200px,#b98a72,transparent 75%),
    radial-gradient(ellipse 70px 80px at 360px 190px,#a97b60,transparent 75%),
    linear-gradient(135deg,#141414,#1f1b1a 55%,#182826)}
.story-inset{left:42px;top:1150px;width:179px;height:195px;border-radius:10px;border:4px solid var(--white);
  background:
    radial-gradient(ellipse 40px 70px at 120px 120px,#8fc7c4,transparent 75%),
    radial-gradient(ellipse 40px 70px at 60px 130px,#2c2c2c,transparent 75%),
    linear-gradient(160deg,#c5c8bd,#8b9186 60%,#6c7069)}
.story-text{position:absolute;left:591px;top:782px;width:472px}
.story-text h2{font-size:39px;font-weight:500;line-height:46px;text-transform:uppercase;margin-top:18px;color:var(--ink)}
.story-text h2 span{color:var(--muted)}
.story-text p{font-size:18.5px;line-height:32.3px;margin-top:52px;color:var(--text)}
.story-cta{left:591px;top:1280px;width:221px;height:34px}

/* who we serve */
.serve{position:absolute;left:0;top:1454px;width:1200px;height:724px;clip-path:polygon(0 0,100% 0,100% 86%,50% 100%,0 86%);
  background:
    linear-gradient(90deg,#263f7c 0%,#2b4784 38%,rgba(43,71,132,.55) 50%,rgba(43,71,132,0) 62%),
    radial-gradient(ellipse 120px 140px at 560px 250px,#c49478,transparent 75%),
    radial-gradient(ellipse 130px 150px at 930px 190px,#5c3a2a,transparent 75%),
    radial-gradient(ellipse 260px 260px at 620px 560px,#2f6fd0,transparent 75%),
    radial-gradient(ellipse 260px 300px at 1010px 480px,#2d6ed4,transparent 75%),
    linear-gradient(90deg,#6f7a8c,#9aa1a8 50%,#8a9a6c 80%,#6f7f5c)}
.serve-text{position:absolute;left:105px;top:72px;width:540px;color:var(--white)}
.serve-text .eyebrow{color:var(--white)}
.serve-text h2{font-size:38px;font-weight:500;line-height:46px;text-transform:uppercase;margin-top:20px}
.serve-text p{font-size:14px;line-height:24px;margin-top:16px;color:#dfe5f0;width:520px}
.serve-text h3{font-size:27px;font-weight:500;margin-top:26px}
.serve-list{list-style:none;margin-top:10px}
.serve-list li{display:flex;align-items:center;gap:14px;font-size:19px;height:43px;color:#eef1f7}
.serve-cta{left:105px;top:555px;width:220px;height:32px;background:var(--accent)}

/* services */
.sec-title{position:absolute;left:0;width:1200px;text-align:center;font-size:39px;font-weight:500;text-transform:uppercase;color:var(--ink)}
.sec-title span{color:var(--blue)}
.rule{position:absolute;height:4px;background:var(--blue);left:563px;width:74px}
.card{position:absolute;top:2374px;width:240px;height:176px;background:var(--white);box-shadow:0 2px 10px rgba(0,0,0,.14);text-align:center;font-size:20px;font-weight:500;line-height:24px;padding-top:20px}
.card svg{position:absolute;left:80px;top:82px}
.services-cta{left:504px;top:2596px;width:192px;height:34px}

/* mission */
.mission{position:absolute;left:0;top:2725px;width:1200px;height:716px;background:var(--grey)}
.mission-text{position:absolute;left:110px;top:138px;width:450px}
.mission-text h2{font-size:40px;font-weight:600;color:#3a3a3a;text-transform:uppercase;margin-top:8px}
.point{margin-top:30px}
.point h3{font-size:23px;font-weight:500;color:var(--ink);position:relative;padding-left:23px}
.point h3::before{content:"";position:absolute;left:0;top:9px;width:8px;height:8px;border-radius:50%;background:var(--navy)}
.point p{font-size:15px;line-height:24px;color:#404040;margin-top:8px;padding-left:23px}
.mission-cta{left:110px;top:545px;width:220px;height:33px}
.mission-photo{left:611px;top:98px;width:478px;height:520px;border-radius:14px;
  background:
    radial-gradient(ellipse 110px 220px at 170px 380px,#f4f4f4,transparent 75%),
    radial-gradient(ellipse 120px 220px at 370px 400px,#e3e3e6,transparent 75%),
    radial-gradient(ellipse 50px 60px at 170px 130px,#d9b8a0,transparent 75%),
    radial-gradient(ellipse 60px 70px at 360px 250px,#3a2e2a,transparent 75%),
    linear-gradient(120deg,#f2f3f4,#e2e5e8 50%,#d5d7d9)}

/* network */
.rule.sky{background:var(--sky)}
.partner{position:absolute;top:3636px;width:252px;height:153px;background:var(--white);box-shadow:0 2px 10px rgba(0,0,0,.12);display:flex;align-items:center;justify-content:center}
.partner .mark{background:var(--badge)}

/* cta */
.join{position:absolute;left:177px;top:3912px;width:846px;height:370px;border-radius:22px;background:linear-gradient(180deg,#1d54c4,#2a5fb8 60%,#2a5aa0);text-align:center;color:var(--white)}
.join .kicker{font-size:19px;margin-top:32px;color:#dbe3f5}
.join h2{font-size:38px;font-weight:500;line-height:39px;text-transform:uppercase;margin-top:22px}
.join h2 span{color:#c9cdd6}
.join p{font-size:14px;line-height:22px;width:560px;margin:18px auto 0;color:#dfe6f5}
.join-cta{left:312px;top:307px;width:219px;height:35px;background:var(--black)}
.join-cta::after{width:6px;height:6px}
.join .arrow{position:absolute;top:210px}

/* footer */
.footer-shape{position:absolute;left:0;top:4350px}
.contact{position:absolute;left:110px;display:flex;gap:16px;color:var(--white);font-size:13px;line-height:16px}
.contact .ico{width:34px;height:34px;border-radius:6px;background:var(--navy);display:flex;align-items:center;justify-content:center;flex:none}
.contact b{font-weight:700;display:block}
.foot-brand{position:absolute;left:372px;top:4530px;display:flex;align-items:center;gap:14px}
.foot-brand .brand-mark{width:56px;height:56px}
.foot-brand .brand-name{font-size:28px}
.foot-brand .brand-name small{font-size:11px}
.foot-links{position:absolute;left:718px;font-size:13px;color:var(--white);display:flex;gap:20px;text-transform:uppercase}
.social{position:absolute;left:531px;top:4602px;display:flex;gap:14px}
.social span{width:14px;height:14px;border-radius:50%;border:2px solid var(--white)}
.legal{position:absolute;top:4697px;font-size:11px;color:#cfcfcf}
.legal a{color:#cfcfcf;text-decoration:underline}
</style>
</head>
<body>

<header class="site-nav">
  <div class="brand"><span class="brand-mark"></span><span class="brand-name">Amber Crest<small>Health and Wellness Group</small></span></div>
  <nav class="nav-links"><span class="active">Home</span><span>About Us</span><span>Services</span><span>Our Team</span><span>Join Our Team</span><span>Contact</span><span>FAQ</span></nav>
  <a class="btn nav-cta">Book an Appointment</a>
</header>

<section class="hero" role="img" aria-label="Smiling first responder in a red jacket outdoors among autumn trees">
  <div class="hero-shade"></div>
  <h1 class="hero-title">Helping those who<em>help others</em></h1>
  <p class="hero-sub">Providing holistic, trauma-informed wellness and rehabilitation<br>care for first responders and healthcare professionals.</p>
  <a class="btn hero-cta small-dot">Explore our services</a>
</section>
<svg class="hero-edge" width="1200" height="140" viewBox="0 0 1200 140">
  <polygon points="0,12 600,115 1200,12 1200,40 600,122 0,40" fill="#2c5c9a"/>
  <polygon points="0,34 600,120 1200,34 1200,140 0,140" fill="#fff"/>
</svg>
<div class="badge"><span></span></div>

<section class="story">
  <div class="photo story-main" role="img" aria-label="Paramedic and nurse giving each other a high five"></div>
  <div class="photo story-inset" role="img" aria-label="Caregiver in scrubs walking with an older man"></div>
  <div class="story-text">
    <div class="eyebrow">Our Story &amp; Mission</div>
    <h2>Redefining wellness<br><span>for those who serve.</span></h2>
    <p>At Amber Crest Health and Wellness Group, we believe in helping those who dedicate their lives to helping others. Founded by a team of mental health and wellness professionals, our centre was built on the principles of compassion, evidence-based care, and community connection. Our mission is to provide a safe, restorative environment where healing, growth, and resilience thrive.</p>
  </div>
  <a class="btn story-cta">Learn more about us</a>
</section>

<section class="serve" role="img" aria-label="Two smiling volunteers in blue vests with arms around each other">
  <div class="serve-text">
    <div class="eyebrow">Who We Serve</div>
    <h2>Supporting those<br>who serve others</h2>
    <p>We proudly support individuals who face extraordinary demands in their daily work and life. Our trauma-informed approach ensures that each person receives personalized, respectful, and confidential care.</p>
    <h3>Groups Served:</h3>
    <ul class="serve-list">
      <li><svg width="22" height="16" viewBox="0 0 22 16"><path d="M2 8l6 6L20 2" stroke="#35a66b" stroke-width="4" fill="none"/></svg>First Responders (Police, Fire, Paramedics, Dispatch)</li>
      <li><svg width="22" height="16" viewBox="0 0 22 16"><path d="M2 8l6 6L20 2" stroke="#35a66b" stroke-width="4" fill="none"/></svg>Healthcare Professionals &amp; Caregivers</li>
      <li><svg width="22" height="16" viewBox="0 0 22 16"><path d="M2 8l6 6L20 2" stroke="#35a66b" stroke-width="4" fill="none"/></svg>Veterans &amp; Military Members</li>
      <li><svg width="22" height="16" viewBox="0 0 22 16"><path d="M2 8l6 6L20 2" stroke="#35a66b" stroke-width="4" fill="none"/></svg>General Public seeking mental wellness</li>
    </ul>
  </div>
  <a class="btn serve-cta">Explore our services</a>
</section>

<section class="services">
  <h2 class="sec-title" style="top:2268px">Our holistic <span>wellness</span> services</h2>
  <div class="rule" style="top:2322px"></div>
  <div class="card" style="left:110px">Mental Health<br>Therapy
    <svg width="80" height="80" viewBox="0 0 80 80" aria-hidden="true">
      <path d="M8 10h64a6 6 0 016 6v36a6 6 0 01-6 6H32l-16 14V58H8a6 6 0 01-6-6V16a6 6 0 016-6z" fill="#000"/>
      <path d="M40 48s-16-9-16-19a8 8 0 0116-3 8 8 0 0116 3c0 10-16 19-16 19z" fill="#fff"/>
    </svg>
  </div>
  <div class="card" style="left:356px">Salt &amp; Sound<br>Therapy
    <svg width="80" height="80" viewBox="0 0 80 80" aria-hidden="true">
      <path d="M40 4v10M22 10l5 8M58 10l-5 8M10 24l8 5M70 24l-8 5" stroke="#000" stroke-width="4" stroke-linecap="round"/>
      <path d="M40 26c-16 0-24 22-24 34 0 10 10 16 24 16s24-6 24-16c0-12-8-34-24-34z" fill="#000"/>
      <circle cx="40" cy="64" r="6" fill="none" stroke="#fff" stroke-width="3"/>
    </svg>
  </div>
  <div class="card" style="left:603px;padding-top:30px">Neurofeedback
    <svg width="80" height="80" viewBox="0 0 80 80" aria-hidden="true">
      <rect x="26" y="4" width="50" height="36" rx="4" fill="#000"/>
      <path d="M44 40l-6 12 16-12z" fill="#000"/>
      <path d="M34 15h34M34 23h34M34 31h22" stroke="#fff" stroke-width="3"/>
      <circle cx="22" cy="58" r="16" fill="#000"/>
      <path d="M22 44v28M10 58h24" stroke="#fff" stroke-width="2.5"/>
    </svg>
  </div>
  <div class="card" style="left:849px;padding-top:38px">OT &amp; Rehabilitation
    <svg width="80" height="80" viewBox="0 0 80 80" aria-hidden="true">
      <rect x="26" y="4" width="50" height="36" rx="4" fill="#000"/>
      <path d="M44 40l-6 12 16-12z" fill="#000"/>
      <path d="M34 15h34M34 23h34M34 31h22" stroke="#fff" stroke-width="3"/>
      <circle cx="22" cy="58" r="16" fill="#000"/>
      <path d="M22 44v28M10 58h24" stroke="#fff" stroke-width="2.5"/>
    </svg>
  </div>
  <a class="btn services-cta">View all services</a>
</section>

<section class="mission">
  <div class="mission-text">
    <div class="eyebrow">Mission &amp; Vision</div>
    <h2>Our guiding purpose</h2>
    <div class="point"><h3>Mission Statement</h3><p>To provide compassionate, trauma-informed care that empowers individuals to heal, recover, and reconnect — physically, emotionally, and mentally.</p></div>
    <div class="point"><h3>Vision Statement:</h3><p>To become the Lakeshore region's leading centre for integrated mental health and wellness, fostering community resilience and advancing care for those who serve others.</p></div>
  </div>
  <a class="btn mission-cta small-dot">Book an appointment</a>
  <div class="photo mission-photo" role="img" aria-label="Therapist resting a hand on a calm young woman's chest in a bright room"></div>
</section>

<section class="network">
  <h2 class="sec-title" style="top:3542px">Our community network</h2>
  <div class="rule sky" style="top:3597px"></div>
  <div class="partner" style="left:85px"><div class="mark" style="width:150px;height:36px;border-radius:18px"></div></div>
  <div class="partner" style="left:344px"><div class="mark" style="width:60px;height:60px;border-radius:50%"></div></div>
  <div class="partner" style="left:603px"><div class="mark" style="width:140px;height:40px;border-radius:8px"></div></div>
  <div class="partner" style="left:863px"><div class="mark" style="width:56px;height:56px;border-radius:10px"></div></div>
</section>

<section class="join">
  <div class="kicker">24/7 Support &amp; Reliability</div>
  <h2>Join us in supporting<br>mental health and<br><span>wellness</span></h2>
  <p>Whether you're seeking support, exploring partnership opportunities, or looking to join our growing team, we welcome you to be part of our mission. Let's create a healthier, more resilient community together.</p>
  <svg class="arrow" style="left:80px" width="90" height="100" viewBox="0 0 90 100"><path d="M8 5 Q10 70 80 90 M60 80 l20 10 -12 -18" stroke="#9fb4dc" stroke-width="3" fill="none"/></svg>
  <svg class="arrow" style="right:80px" width="90" height="100" viewBox="0 0 90 100"><path d="M82 5 Q80 70 10 90 M30 80 l-20 10 12 -18" stroke="#9fb4dc" stroke-width="3" fill="none"/></svg>
  <a class="btn join-cta">Book an appointment</a>
</section>

<footer>
  <svg class="footer-shape" width="1200" height="393" viewBox="0 0 1200 393">
    <polygon points="0,150 600,0 1200,150 1200,165 600,25 0,165" fill="#9a9a9a"/>
    <polygon points="0,165 600,25 1200,165 1200,180 600,40 0,180" fill="#2c5c9a"/>
    <polygon points="0,180 600,40 1200,180 1200,393 0,393" fill="#000"/>
  </svg>
  <div class="contact" style="top:4535px"><span class="ico"><svg width="16" height="16" viewBox="0 0 24 24"><path d="M6 2l4 4-2 3c1 3 4 6 7 7l3-2 4 4-3 4C10 21 3 14 2 5z" fill="#fff"/></svg></span><div><b>Call Us:</b>01234 560718</div></div>
  <div class="contact" style="top:4592px"><span class="ico"><svg width="16" height="14" viewBox="0 0 24 20"><rect x="2" y="2" width="20" height="16" fill="none" stroke="#fff" stroke-width="2"/><path d="M2 3l10 8 10-8" stroke="#fff" stroke-width="2" fill="none"/></svg></span><div><b>Email us:</b>contact@ambercrest.example</div></div>
  <div class="contact" style="top:4652px"><span class="ico"><svg width="14" height="18" viewBox="0 0 20 26"><path d="M10 1a8 8 0 018 8c0 6-8 16-8 16S2 15 2 9a8 8 0 018-8z" fill="none" stroke="#fff" stroke-width="2"/><circle cx="10" cy="9" r="3" fill="#fff"/></svg></span><div><b>Our Location:</b>Harbour Falls, Ontario –<br>Opening March 2026</div></div>
  <div class="foot-brand"><span class="brand-mark"></span><span class="brand-name">Amber Crest<small>Health and Wellness Group</small></span></div>
  <div class="social"><span></span><span></span><span></span><span></span></div>
  <div class="foot-links" style="top:4540px"><span>Home</span><span>About Us</span><span>Services</span></div>
  <div class="foot-links" style="top:4575px"><span>Our Team</span><span>Join Our Team</span><span>Contact</span><span>Contact</span></div>
  <div class="legal" style="left:464px">© 2025 <b style="color:#fff">Amber Crest</b>. All rights reserved.</div>
  <div class="legal" style="left:802px"><a>PRIVACY POLICY</a></div>
  <div class="legal" style="left:981px"><a>TERMS OF USE</a></div>
</footer>

</body>
</html>
```